Design a helpdesk ticketing platform *

We are launching a helpdesk ticketing platform. Very much like quellbox.com, merrylark.com, pivolta.com, brisktray.com etc. We have a full mid-fidelity prototype built and we want someone to build the full fidelity of the product.

You can view the full mid-fidelity prototype here: https://lnk.vexora.net/Qa8Lpw

The best way moving forward is to just design the following 4 pages

- Main Dashboard https://lnk.vexora.net/81hRtd
- All tickets https://lnk.vexora.net/jwNoEb
- Viewing a ticket https://lnk.vexora.net/Ys4VmK
- Contacts https://lnk.vexora.net/pHeXuo

Target Market(s)

Small business owners

Industry/Entity Type

Saas

Number of Pages Required

4 page

Font styles to use
Serif
Sans Serif

Colors

Designer to choose colors to be used in the design.

Requirements
Must have
• Must follow the prototype exactly. We are not looking for any UX changes. We want the designe xactly as the prototype is. We are only looking for design ideas.
Should not have
• modern, clean. We'd love to see the primary color as yellow, purple, orange, green or blue. You choose which one you think looks best and go with that.

```html
<!DOCTYPE html>
<html lang="en">
<head>
<meta charset="utf-8">
<title>ticketnest – Contact</title>
<link href="https://fonts.googleapis.com/css2?family=Montserrat:wght@400;500;600;700&display=swap" rel="stylesheet">
<style>
:root{
  --side-top:#1c84a6;
  --side-bottom:#174a87;
  --side-active:#16507a;
  --accent:#1b8ec0;
  --btn-a:#f08f1c;
  --btn-b:#e6c41a;
  --ink:#222831;
  --muted:#6d727a;
  --line:#e3e5e8;
  --band:#f2f3f5;
  --danger:#d3231f;
  --white:#ffffff;
}
*{box-sizing:border-box;margin:0;padding:0}
html,body{width:1200px;height:790px;overflow:hidden;background:var(--white)}
body{font-family:"Montserrat",sans-serif;color:var(--ink);position:relative}
.sidebar{position:absolute;left:0;top:0;width:244px;height:790px;background:linear-gradient(180deg,var(--side-top),var(--side-bottom));color:var(--white)}
.brand{position:absolute;left:20px;top:22px;font-size:22px;font-weight:500;letter-spacing:.2px}
.menu-toggle{position:absolute;left:203px;top:28px}
.new-ticket{position:absolute;left:20px;top:63px;width:204px;height:38px;background:linear-gradient(90deg,var(--btn-a),var(--btn-b));display:flex;align-items:center;justify-content:center;gap:6px;font-size:12.5px;font-weight:600}
.side-divider{position:absolute;left:0;top:117px;width:244px;border-top:1px solid rgba(255,255,255,.15)}
.nav{position:absolute;top:141px;left:0;width:244px;list-style:none}
.nav li{height:41px;margin-bottom:10px;display:flex;align-items:center;padding-left:20px;font-size:13.5px;position:relative}
.nav li svg.icon{margin-right:10px}
.nav li.active{background:var(--side-active);font-weight:700}
.nav .caret{position:absolute;right:18px;top:17px}
.topbar{position:absolute;left:244px;top:0;right:0;height:69px;display:flex;align-items:center;padding-left:19px;border-bottom:1px solid var(--line)}
.crumbs{font-size:18px;font-weight:500}
.crumbs .current{color:var(--accent)}
.search{position:absolute;left:637px;top:19px;width:204px;height:33px;border:1px solid #c9ccd1;display:flex;align-items:center;padding-left:10px;gap:8px;font-size:11.5px;color:var(--muted)}
.avatar-me{position:absolute;left:859px;top:19px;width:34px;height:34px;border-radius:50%;background:var(--accent);color:var(--white);font-size:13px;display:flex;align-items:center;justify-content:center}
.more{position:absolute;left:910px;top:33px;display:flex;gap:4px}
.more span{width:5px;height:5px;border-radius:50%;background:#8c9098}
.toolbar{position:absolute;left:244px;top:69px;right:0;height:48px;background:var(--band);border-bottom:1px solid var(--line)}
.tool{position:absolute;top:8px;height:32px;border:1px solid #d3d6da;background:var(--white);display:flex;align-items:center;justify-content:center;gap:5px;font-size:11px}
.profile{position:absolute;left:244px;top:117px;width:262px;height:673px;border-right:1px solid var(--line);padding:19px 0 0 20px}
.initials{width:44px;height:44px;border-radius:50%;background:var(--accent);color:var(--white);font-size:17px;display:flex;align-items:center;justify-content:center;margin-left:-2px}
.name{font-size:19px;font-weight:500;margin-top:16px}
.email{font-size:11.5px;color:var(--muted);margin-top:3px}
.field{margin-top:20px}
.field dt{font-size:12px;font-weight:600}
.field dd{font-size:12px;color:var(--muted);margin-top:5px;line-height:15.5px}
.field + .field{margin-top:16px}
.file{text-decoration:underline;display:inline-flex;align-items:center;gap:7px}
.tickets{position:absolute;left:506px;top:117px;right:0;bottom:0}
.tabs{height:50px;border-bottom:1px solid var(--line);position:relative}
.check{width:14px;height:14px;border:1px solid #c9ccd1;border-radius:2px;background:var(--white);position:absolute}
.select-all{position:absolute;left:40px;top:19px;font-size:10px}
.tab{position:absolute;top:17px;font-size:13.5px}
.tab.on{font-weight:600}
.tab.on::after{content:"";position:absolute;left:-6px;right:-6px;top:29px;height:3px;background:var(--accent)}
.thead{height:43px;background:var(--band);position:relative;font-size:11.5px;font-weight:600}
.row{height:56px;border-bottom:1px solid var(--line);position:relative;font-size:12.5px}
.cell{position:absolute;top:50%;transform:translateY(-50%);display:flex;align-items:center;gap:7px;white-space:nowrap}
.past{color:var(--danger)}
.kebab{position:absolute;left:671px;top:20px;display:flex;flex-direction:column;gap:3px}
.kebab span{width:4px;height:4px;border-radius:50%;background:#8c9098}
</style>
</head>
<body>
<aside class="sidebar">
  <div class="brand">ticketnest</div>
  <svg class="menu-toggle" width="22" height="16" viewBox="0 0 22 16"><path d="M0 1h22M0 8h22M0 15h22" stroke="#fff" stroke-width="2"/></svg>
  <div class="new-ticket">New Ticket <svg width="11" height="11" viewBox="0 0 11 11"><path d="M5.5 0v11M0 5.5h11" stroke="#fff" stroke-width="2"/></svg></div>
  <div class="side-divider"></div>
  <ul class="nav">
    <li><svg class="icon" width="17" height="17" viewBox="0 0 17 17" fill="none" stroke="#fff" stroke-width="1.4"><circle cx="8.5" cy="8.5" r="7.5"/><path d="M8.5 9.5l3-4"/><circle cx="8.5" cy="9.5" r="1"/></svg>Dashboard</li>
    <li><svg class="icon" width="18" height="17" viewBox="0 0 18 17"><path d="M9 1l7 7-8 8-7-7V1z" fill="#fff"/><circle cx="5" cy="5" r="1.5" fill="#1c6f9c"/></svg>Tickets<svg class="caret" width="10" height="6" viewBox="0 0 10 6"><path d="M1 1l4 4 4-4" stroke="#fff" fill="none" stroke-width="1.3"/></svg></li>
    <li class="active"><svg class="icon" width="18" height="14" viewBox="0 0 18 14" fill="none" stroke="#fff" stroke-width="1.5"><rect x="1" y="1" width="16" height="12"/><circle cx="6" cy="6" r="2"/><path d="M3 11c0-2 6-2 6 0M11 5h4M11 8h4"/></svg>Contacts</li>
    <li><svg class="icon" width="18" height="18" viewBox="0 0 18 18" fill="none" stroke="#fff" stroke-width="1.4"><circle cx="9" cy="9" r="3"/><path d="M9 1v3M9 14v3M1 9h3M14 9h3M3.3 3.3l2.1 2.1M12.6 12.6l2.1 2.1M3.3 14.7l2.1-2.1M12.6 5.4l2.1-2.1"/></svg>Admin Settings<svg class="caret" width="10" height="6" viewBox="0 0 10 6"><path d="M1 1l4 4 4-4" stroke="#fff" fill="none" stroke-width="1.3"/></svg></li>
    <li><svg class="icon" width="18" height="14" viewBox="0 0 18 14" fill="none" stroke="#fff" stroke-width="1.5"><rect x="1" y="1" width="16" height="12" rx="1"/><path d="M1 5h16"/></svg>Account &amp; Billing</li>
  </ul>
</aside>

<header class="topbar">
  <div class="crumbs">Contacts / <span class="current">Mara Ellison</span></div>
</header>
<div class="search"><svg width="14" height="14" viewBox="0 0 14 14" fill="none" stroke="#6d727a" stroke-width="1.3"><circle cx="8" cy="6" r="5"/><path d="M4.5 9.5L1 13"/></svg>Search</div>
<div class="avatar-me">RN</div>
<div class="more"><span></span><span></span><span></span></div>

<div class="toolbar">
  <div class="tool" style="left:20px;width:107px"><svg width="9" height="9" viewBox="0 0 9 9"><path d="M4.5 0v9M0 4.5h9" stroke="#222831" stroke-width="1.6"/></svg>New Ticket</div>
  <div class="tool" style="left:134px;width:107px"><svg width="10" height="10" viewBox="0 0 10 10"><path d="M0 10l1-3 6-6 2 2-6 6z" fill="#1b4f8a"/></svg>Add a Note</div>
  <div class="tool" style="left:248px;width:107px"><svg width="10" height="11" viewBox="0 0 10 11" fill="none" stroke="#1b4f8a" stroke-width="1.2"><circle cx="5" cy="3.5" r="2.7"/><path d="M.6 11c0-3 8.8-3 8.8 0"/></svg>Edit Contact</div>
  <div class="tool" style="left:813px;width:122px"><svg width="9" height="11" viewBox="0 0 9 11" fill="none" stroke="#d3231f" stroke-width="1.2"><path d="M0 2h9M3 2V.6h3V2M1.5 2l.6 8.4h4.8L7.5 2M3.6 4v5M5.4 4v5"/></svg>Delete Contact</div>
</div>

<section class="profile">
  <div class="initials">ME</div>
  <div class="name">Mara Ellison</div>
  <div class="email">maraellison@postmeadow.com</div>
  <dl>
    <div class="field"><dt>Title</dt><dd>Marketing Manager</dd></div>
    <div class="field"><dt>Work Phone</dt><dd>119-555-0147</dd></div>
    <div class="field"><dt>Mobile Phone</dt><dd>230-555-0182</dd></div>
    <div class="field"><dt>Level</dt><dd>Expert</dd></div>
    <div class="field"><dt>Attachments</dt><dd><span class="file">Terms.docx <svg width="12" height="10" viewBox="0 0 12 10" fill="none" stroke="#1b8ec0" stroke-width="1.1"><path d="M3 8H2.5a2.3 2.3 0 010-4.6A3.3 3.3 0 019 3a2.5 2.5 0 010 5H9M6 5v4M4.5 7.5L6 9l1.5-1.5"/></svg></span></dd></div>
    <div class="field"><dt>Company</dt><dd>Granite Haulage INC.</dd></div>
    <div class="field"><dt>Address</dt><dd>4820 Alder Row, Brookfield, MO 75610</dd></div>
    <div class="field"><dt>Timezone</dt><dd>Pacific Time (US &amp; Canada)</dd></div>
    <div class="field"><dt>About</dt><dd>Mara is the marketing manager for Granite Haulage INC. She is in charge of 100+ clients for the company</dd></div>
  </dl>
</section>

<section class="tickets">
  <div class="tabs">
    <span class="check" style="left:19px;top:18px"></span>
    <span class="select-all">Select all</span>
    <span class="tab on" style="left:126px">Tickets</span>
    <span class="tab" style="left:221px">Notes</span>
  </div>
  <div class="thead">
    <span class="cell" style="left:46px">Subject</span>
    <span class="cell" style="left:220px">State</span>
    <span class="cell" style="left:338px">Group</span>
    <span class="cell" style="left:460px">Agent</span>
    <span class="cell" style="left:588px">Priority</span>
  </div>

  <div class="row">
    <span class="check" style="left:19px;top:21px"></span>
    <span class="cell" style="left:47px">I can’t reset... (#15)</span>
    <span class="cell past" style="left:219px">Past Due</span>
    <span class="cell" style="left:338px">Sales <svg width="9" height="6" viewBox="0 0 9 6"><path d="M1 1l3.5 3.5L8 1" stroke="#222831" fill="none" stroke-width="1.3"/></svg></span>
    <span class="cell" style="left:460px">Devon <svg width="9" height="6" viewBox="0 0 9 6"><path d="M1 1l3.5 3.5L8 1" stroke="#222831" fill="none" stroke-width="1.3"/></svg></span>
    <span class="cell" style="left:588px">Low <svg width="9" height="6" viewBox="0 0 9 6"><path d="M1 1l3.5 3.5L8 1" stroke="#222831" fill="none" stroke-width="1.3"/></svg></span>
    <span class="kebab"><span></span><span></span><span></span></span>
  </div>
  <div class="row">
    <span class="check" style="left:19px;top:21px"></span>
    <span class="cell" style="left:47px">Close Account (#16)</span>
    <span class="cell" style="left:219px">Closed</span>
    <span class="cell" style="left:338px">Sales <svg width="9" height="6" viewBox="0 0 9 6"><path d="M1 1l3.5 3.5L8 1" stroke="#222831" fill="none" stroke-width="1.3"/></svg></span>
    <span class="cell" style="left:460px">Devon <svg width="9" height="6" viewBox="0 0 9 6"><path d="M1 1l3.5 3.5L8 1" stroke="#222831" fill="none" stroke-width="1.3"/></svg></span>
    <span class="cell" style="left:588px">Low <svg width="9" height="6" viewBox="0 0 9 6"><path d="M1 1l3.5 3.5L8 1" stroke="#222831" fill="none" stroke-width="1.3"/></svg></span>
    <span class="kebab"><span></span><span></span><span></span></span>
  </div>
  <div class="row">
    <span class="check" style="left:19px;top:21px"></span>
    <span class="cell" style="left:47px">Setup Agent (#15)</span>
    <span class="cell" style="left:219px">Closed</span>
    <span class="cell" style="left:338px">Sales <svg width="9" height="6" viewBox="0 0 9 6"><path d="M1 1l3.5 3.5L8 1" stroke="#222831" fill="none" stroke-width="1.3"/></svg></span>
    <span class="cell" style="left:460px">Devon <svg width="9" height="6" viewBox="0 0 9 6"><path d="M1 1l3.5 3.5L8 1" stroke="#222831" fill="none" stroke-width="1.3"/></svg></span>
    <span class="cell" style="left:588px">Low <svg width="9" height="6" viewBox="0 0 9 6"><path d="M1 1l3.5 3.5L8 1" stroke="#222831" fill="none" stroke-width="1.3"/></svg></span>
    <span class="kebab"><span></span><span></span><span></span></span>
  </div>
</section>
</body>
</html>
```